Web Design Project

We are an online tax Continuing education provider. We provide online courses for tax preparers. We want the front end page to be user friendly and for the buyer to know exactly what they are looking at. We want a front end page to look smiliar www.marblequill.com. It should have a similar feel to this one.
Our website address will be www.7382LQ.com
We currently have another website that is www.LedgerNoks.com but we do not want it to look like this. We want a different look but same information.
We have a logo already which is attached. We don't have specific colors in mind for the front page but don't want it to be too busy looking. It should stand out but not too simple either.
Target Market(s)
Tax Preparers. More serious and professional but these folks are usually not tech savy. Simple, easy to use, and functional is key.
Industry/Entity Type
Education
Requirements
Must have
- Use standard HTML & CSS. NO other coding is needed.
We are looking for 5-7 pages including Home page, log in, FAQ.
Please look at our current website www.LedgerNoks.com and also www.marblequill.com

```html
<!DOCTYPE html>
<html lang="en">
<head>
<meta charset="utf-8">
<title>7382LQ – Continuing Education Made Simple</title>
<link rel="stylesheet" href="https://fonts.googleapis.com/css2?family=Cabin:ital,wght@0,400;0,600;1,400&family=Arimo:wght@700&family=Ubuntu:wght@500;700&display=swap">
<style>
:root{
  --navy:#1b3460;
  --bar-top:#fafafa;
  --bar-bottom:#e4e4e4;
  --ink:#1a1a1a;
  --muted:#7a7a7a;
  --text:#2b2b2b;
  --title-blue:#2d3f8c;
  --fast:#2a7bbf;
  --easy:#3a9a2a;
  --cost:#f08c1a;
  --orange:#ff8a00;
  --olive-top:#c9dc52;
  --olive-bottom:#98b22a;
  --cta:#19a2cf;
  --box-line:#d4d4d4;
  --quote-red:#e02020;
}
*{box-sizing:border-box;margin:0;padding:0}
html,body{width:1052px;height:1200px;overflow:hidden}
body{
  background:linear-gradient(to bottom,var(--bar-top) 0,var(--bar-bottom) 29px,var(--navy) 29px,var(--navy) 236px,#d8d8d8 236px,#fff 330px,#fff 100%);
  font-family:"Cabin",sans-serif;color:var(--text);position:relative;
}
a{text-decoration:none}
.wrap{position:absolute;left:123px;width:806px}
.brand{position:absolute;left:123px;top:0;width:141px;height:101px;border-radius:0 0 4px 4px;
  background:linear-gradient(#fff,#e3e3e3);box-shadow:0 1px 4px rgba(0,0,0,.4);
  display:flex;align-items:center;justify-content:center;gap:7px}
.brand-dot{width:13px;height:13px;border-radius:50%;background:var(--navy)}
.brand-name{font-size:24px;font-weight:600;color:var(--navy)}
.main-nav{position:absolute;right:123px;top:7px;display:flex;gap:33px}
.main-nav a{font-size:14px;color:var(--ink);letter-spacing:.3px}
.contact{position:absolute;right:123px;top:55px;display:flex;gap:12px;align-items:center;color:#fff;font-family:"Ubuntu",sans-serif}
.contact-lines{line-height:1}
.contact-phone{font-size:23px;font-weight:700}
.contact-mail{font-size:17px;font-weight:500;margin-top:3px}
.card{top:126px;height:580px;background:#fff;border-radius:4px;box-shadow:0 1px 3px rgba(0,0,0,.25)}
.headline{text-align:center;font-size:44px;font-weight:400;color:var(--ink);margin-top:22px}
.perks{display:flex;justify-content:center;gap:48px;margin-top:8px;font-size:23px}
.perk{display:flex;align-items:center;gap:12px}
.perk-fast{color:var(--fast)}.perk-easy{color:var(--easy)}.perk-cost{color:var(--cost)}
.tagline{text-align:center;font-size:28px;color:var(--muted);margin-top:4px}
.book{position:absolute;top:88px;width:130px;height:66px;border-radius:6px;
  background:linear-gradient(160deg,#f4f4f4,#bdbdbd)}
.book-left{left:20px}.book-right{right:20px}
.packages{position:absolute;top:195px;left:17px;right:17px;display:flex;gap:16px}
.package{width:247px;height:382px;background:linear-gradient(#f7f7f7,#ededed);border:1px solid var(--box-line);border-radius:4px;padding:14px 14px 0 15px;position:relative}
.package-title{font-size:18px;font-weight:400;color:var(--title-blue);line-height:1.2}
.package-list{list-style:none;margin-top:11px}
.package-list li{font-size:12.5px;line-height:1.15;padding-left:16px;position:relative;margin-bottom:8px}
.package-list li::before{content:"➪";position:absolute;left:0;color:#9a9a9a;font-size:10px}
.price{position:absolute;left:69px;top:217px;width:107px;height:107px;border-radius:50%;background:var(--orange);
  color:#fff;font-family:"Arimo",sans-serif;font-weight:700;font-size:26px;text-align:center;padding-top:27px}
.provider{position:absolute;left:22px;top:281px;width:202px;height:29px;border-radius:15px;
  background:linear-gradient(var(--olive-top),var(--olive-bottom));font-size:12.5px;color:#1a1a1a;text-align:center;line-height:29px}
.more{position:absolute;left:37px;top:327px;width:171px;height:36px;background:var(--cta);color:#fff;border-radius:3px;
  font-family:"Arimo",sans-serif;font-weight:700;font-size:16px;text-align:center;line-height:36px}
.rule{position:absolute;left:123px;width:806px;height:1px;background:linear-gradient(to right,transparent,#d0d0d0,transparent)}
.testimonial{top:756px;text-align:center;font-style:italic;font-size:13.5px;line-height:1.5;color:#333;padding:0 24px}
.testimonial cite{display:block;color:var(--quote-red)}
.bulletin{position:absolute;left:346px;top:862px;width:361px;height:40px;background:var(--cta);color:#fff;border-radius:3px;font-size:18px;text-align:center;line-height:40px}
.arrow{position:absolute;left:712px;top:876px}
.irs-link{top:913px;text-align:center;font-size:21px;color:var(--ink)}
.irs-link span{color:var(--muted)}
.site-footer{top:976px;height:158px;background:#f0f0f0;border:1px solid var(--box-line);border-radius:4px;padding:27px 0 0 32px;display:flex}
.foot-col{list-style:none;font-size:12px;line-height:1.2}
.foot-col li{margin-bottom:7px;color:#222}
.col-a{width:148px}.col-b{width:224px}.col-c{width:264px}
.col-b li{margin-bottom:8px}
.bottom{top:1146px;height:40px;display:flex;align-items:center;justify-content:space-between}
.accreditor{display:flex;align-items:center;gap:7px;font-size:9px;color:#777;line-height:1.15;text-transform:uppercase}
.badge-square{width:36px;height:36px;border:4px solid #a99b74;background:#e9e6dc}
.copyright{font-size:12px;color:#555;margin-left:70px}
.trust{display:flex;align-items:center;gap:12px}
.badge-seal{width:69px;height:38px;background:linear-gradient(#f3d27a,#c48a2a);border:1px solid #8a6a20}
.partner{display:flex;align-items:center;gap:5px;font-size:22px;font-weight:600;color:#1a6a2a}
.partner-dot{width:10px;height:10px;border-radius:50%;background:#1a6a2a}
</style>
</head>
<body>
<header>
  <a class="brand" href="#"><span class="brand-dot"></span><span class="brand-name">7382LQ</span></a>
  <nav class="main-nav"><a href="#">HOME</a><a href="#">COURSES</a><a href="#">FAQ</a><a href="#">CONTACT</a><a href="#">SIGN IN</a></nav>
  <div class="contact">
    <svg width="27" height="40" viewBox="0 0 27 40" aria-hidden="true"><rect x="1" y="1" width="25" height="38" rx="5" fill="#d8d8d8"/><rect x="5" y="7" width="17" height="22" fill="#9a9a9a"/><circle cx="13.5" cy="34" r="2.2" fill="#9a9a9a"/></svg>
    <div class="contact-lines"><div class="contact-phone">800-555-0142</div><div class="contact-mail">info@7382lq.com</div></div>
  </div>
</header>

<main>
  <section class="wrap card">
    <h1 class="headline">Continuing Education Made Simple!</h1>
    <div class="perks">
      <span class="perk perk-fast"><svg width="24" height="24" viewBox="0 0 24 24" aria-hidden="true"><rect x="1" y="4" width="19" height="19" fill="#eee" stroke="#888" stroke-width="1.5"/><path d="M5 13l5 5 12-16" fill="none" stroke="#555" stroke-width="3"/></svg>Fast</span>
      <span class="perk perk-easy"><svg width="24" height="24" viewBox="0 0 24 24" aria-hidden="true"><rect x="1" y="4" width="19" height="19" fill="#eee" stroke="#888" stroke-width="1.5"/><path d="M5 13l5 5 12-16" fill="none" stroke="#555" stroke-width="3"/></svg>Easy</span>
      <span class="perk perk-cost"><svg width="24" height="24" viewBox="0 0 24 24" aria-hidden="true"><rect x="1" y="4" width="19" height="19" fill="#eee" stroke="#888" stroke-width="1.5"/><path d="M5 13l5 5 12-16" fill="none" stroke="#555" stroke-width="3"/></svg>Low Cost</span>
    </div>
    <p class="tagline">Completely Online! "Self-paced"</p>
    <div class="book book-left" role="img" aria-label="Open silver book illustration"></div>
    <div class="book book-right" role="img" aria-label="Open silver book illustration"></div>

    <div class="packages">
      <article class="package">
        <h2 class="package-title">15-Hour Package for IRS Registered Tax-Preparer CE</h2>
        <ul class="package-list">
          <li>Ethics (2 hrs CE Credit)</li>
          <li>Charitable Contributions 101<br>(3 hrs CE Credit)</li>
          <li>Earned Income Credit<br>(2 hrs CE Credit)</li>
          <li>Deducting Transportation Expenses<br>(2 hrs CE Credit)</li>
        </ul>
        <div class="price">$42</div>
        <div class="provider">Provided by 7382 Learning, LLC</div>
        <a class="more" href="#">FIND OUT MORE</a>
      </article>
      <article class="package">
        <h2 class="package-title">RTRP Exam Prepration Course 10 CE Credit</h2>
        <ul class="package-list">
          <li>10-HR RTRP Exam Simulator Course</li>
          <li>Study for the RTRP exam and receive CE credit at the same time.</li>
          <li>It is comprised of four full-length practice exams (120 questions each).</li>
          <li>The fourth exam attempts to mimic the actual IRS exam.</li>
        </ul>
        <div class="price">$79.99</div>
        <div class="provider">Provided by 7382 Learning, LLC</div>
        <a class="more" href="#">FIND OUT MORE</a>
      </article>
      <article class="package">
        <h2 class="package-title">Combo Package RTRP Exam Prep Course &amp; CE</h2>
        <ul class="package-list">
          <li>10-HR RTRP Exam Simulator Course</li>
          <li>Study for the RTRP exam and receive CE credit at the same time.</li>
          <li>It is comprised of four full-length practice exams (120 questions each).</li>
          <li>The fourth exam attempts to mimic the actual IRS exam.</li>
        </ul>
        <div class="price">$99.90</div>
        <div class="provider">Provided by 7382 Learning, LLC</div>
        <a class="more" href="#">FIND OUT MORE</a>
      </article>
    </div>
  </section>

  <div class="rule" style="top:740px"></div>
  <blockquote class="wrap testimonial">The class was very convenient because I work crazy hours ... the pace was great. I learned some laws that I wasn't aware of to help my clients. I highly recommend this course to others. Thank you!!<cite>- Danielle.Tx</cite></blockquote>
  <div class="rule" style="top:828px"></div>

  <a class="bulletin" href="#">RTRP Test Candidate Information Bullrtin</a>
  <svg class="arrow" width="40" height="42" viewBox="0 0 40 42" aria-hidden="true"><path d="M36 40C34 22 22 12 4 8" fill="none" stroke="#555" stroke-width="1.3" stroke-dasharray="3 3"/><path d="M10 3L3 8l7 5" fill="none" stroke="#555" stroke-width="1.5"/></svg>
  <p class="wrap irs-link">IRS Latest Information Link <span>( Click button to open IRS document or link)</span></p>
</main>

<footer>
  <nav class="wrap site-footer">
    <ul class="foot-col col-a"><li>Home</li><li>Courses</li><li>FAQ</li><li>Contact</li><li>Sign In</li></ul>
    <ul class="foot-col col-b"><li>IRS Approved Provider</li><li>Certificate of Completion</li><li>Professional!</li><li>Self-paced Low Cost</li><li>Fast &amp; Easy Convenience</li></ul>
    <ul class="foot-col col-c"><li>15-Hour Package for IRS Registered<br>Tax-Preparer CE</li><li>RTRP Exam Prepration Course 10 CE<br>Credit</li><li>Combo Package RTRP Exam Prep<br>Course &amp; CE</li></ul>
    <ul class="foot-col"><li>Support</li><li>Privacy Policy</li><li>Terms &amp; Conditions</li><li>Contact</li></ul>
  </nav>
  <div class="wrap bottom">
    <div class="accreditor"><span class="badge-square"></span><span>Approved<br>Continuing Education<br>Accreditor</span></div>
    <p class="copyright">Copyright ©2013 7382LQ. All rights reserved.</p>
    <div class="trust"><span class="badge-seal"></span><span class="partner"><span class="partner-dot"></span>LedgerNoks.com</span></div>
  </div>
</footer>
</body>
</html>
```